"Before and After" Infographic

Before and After with CrestWeave MRP

This infographic is intended to show the impact on a manufacturing business transitioning from manual spreadsheet-based planning to using CrestWeave’s Planning & Scheduling software platform.

This should be viewable, readable on a phone and PC.

This is a list of before/after scenarios that are intended to show how our planning and scheduling system improves the manufacturer's business.

BEFORE
Frequent long clean-outs and changeovers take up machine time and lead to lost output
AFTER
Machines run more efficiently, sequencing similar work together to avoid long down-times. Increase output by 20% or more.

BEFORE
Planning personnel spend many hours every day managing schedule changes
AFTER
Schedules are optimized automatically and personnel have time for strategic planning and continuous improvement activities. Save up to 80% of planner time.

BEFORE
Inventory and lead-times are excessive.
AFTER
Flow is streamlined, Inventory and Lead Time are reduced by up to 50%.

BEFORE
Chaotic expediting is rampant, causing inefficiency and late shipments.
AFTER
Accurate, long terms schedule visibility allows for accurate order commitments and on-time shipments. Efficiency and customer service improve, increasing sales and profit margins.

BEFORE
Sales and operations planning decisions about capacity, staffing, overtime, and forecasts are difficult and error prone.
AFTER
Great decisions are made quickly with data-driven what-if simulations to evaluate alternatives against key metrics

We'll also want our logo and company name displayed.

```html
<!DOCTYPE html>
<html lang="en">
<head>
<meta charset="utf-8">
<title>Before and After with CrestWeave MRP</title>
<link rel="stylesheet" href="https://fonts.googleapis.com/css2?family=Fira+Sans:wght@300;400;500;700&display=swap">
<style>
  :root {
    --blue: #1e93d6;
    --blue-soft: #8cc4e8;
    --ink: #333333;
    --number: #666666;
    --band-grey: #efefef;
    --after-bg: #f0f0f0;
    --vs-grey: #6d6e70;
    --rule-grey: #cfcfcf;
    --art-grey-a: #d6d6d6;
    --art-grey-b: #e6e6e6;
    --art-blue-a: #8cc4e8;
    --art-blue-b: #bfdcf1;
    --white: #ffffff;
  }
  * { margin: 0; padding: 0; box-sizing: border-box; }
  html, body { width: 1200px; height: 2699px; overflow: hidden; background: var(--white); }
  body { font-family: "Fira Sans", Arial, sans-serif; color: var(--ink); }
  .canvas { position: relative; width: 1200px; height: 2699px; }

  .brand { position: absolute; top: 52px; left: 0; width: 1200px; text-align: center; }
  .brand-name { display: inline-flex; align-items: center; gap: 12px; font-size: 38px; font-weight: 500; line-height: 48px; color: var(--blue); }
  .brand-mark { width: 24px; height: 24px; background: var(--blue); border-radius: 50%; }
  .brand-url { display: block; margin-top: 4px; font-size: 21px; line-height: 28px; color: var(--ink); }

  .header-band { position: absolute; top: 192px; left: 0; width: 1200px; height: 99px; background: var(--band-grey); }
  .header-band .after-side { position: absolute; left: 590px; top: 0; width: 610px; height: 99px; background: var(--blue); }
  .label { position: absolute; top: 214px; font-size: 44px; line-height: 54px; font-weight: 700; letter-spacing: 1px; }
  .label-before { left: 158px; color: var(--blue); }
  .label-after { left: 720px; color: var(--white); }
  .vs { position: absolute; left: 518px; top: 169px; width: 144px; height: 144px; border-radius: 50%; background: var(--vs-grey); border: 6px solid var(--white); color: var(--white); font-size: 66px; font-weight: 400; display: flex; align-items: center; justify-content: center; }

  .after-column { position: absolute; left: 612px; top: 291px; width: 588px; height: 2408px; background: var(--after-bg); }

  .num { position: absolute; left: 80px; font-size: 72px; line-height: 80px; font-weight: 300; color: var(--number); }
  .art { position: absolute; border-radius: 10px; }
  .art-before { background: linear-gradient(160deg, var(--art-grey-b), var(--art-grey-a)); }
  .art-after { background: linear-gradient(160deg, var(--art-blue-b), var(--art-blue-a)); }
  .before-text, .after-text { position: absolute; font-size: 23px; line-height: 31px; font-weight: 400; }
  .before-text { left: 130px; width: 340px; }
  .after-text { left: 682px; width: 440px; }

  .divider { position: absolute; left: 119px; width: 939px; height: 0; border-top: 2px dashed var(--blue-soft); }
  .divider.first { border-top: none; }
  .divider.first::before { content: ""; position: absolute; left: 0; top: 0; width: 493px; border-top: 2px solid var(--rule-grey); }
  .divider.first::after { content: ""; position: absolute; left: 493px; top: 0; width: 446px; border-top: 2px dashed var(--blue-soft); }
</style>
</head>
<body>
<main class="canvas">
  <header class="brand">
    <span class="brand-name">CrestWeave <span class="brand-mark"></span></span>
    <span class="brand-url">www.crestweave.com</span>
  </header>

  <div class="header-band"><div class="after-side"></div></div>
  <div class="label label-before">BEFORE</div>
  <div class="label label-after">AFTER</div>
  <div class="vs">VS</div>
  <div class="after-column"></div>

  <section class="row row-1">
    <div class="num" style="top:386px">1.</div>
    <div class="art art-before" role="img" aria-label="Line icon of a gear above stacked chevrons" style="left:230px;top:387px;width:121px;height:207px"></div>
    <p class="before-text" style="top:620px">Frequent long clean-outs and changeovers take up machine time and lead to lost output</p>
    <div class="art art-after" role="img" aria-label="Speedometer gauge icon showing high output" style="left:716px;top:450px;width:313px;height:108px"></div>
    <p class="after-text" style="top:588px">Machines run more efficiently, sequencing similar work together to avoid long down-times. Increase output by 20% or more.</p>
    <div class="divider first" style="top:779px"></div>
  </section>

  <section class="row row-2">
    <div class="num" style="top:894px">2.</div>
    <div class="art art-before" role="img" aria-label="Line icon of a hand writing on a schedule sheet" style="left:216px;top:860px;width:176px;height:151px"></div>
    <p class="before-text" style="top:1037px">Planning personnel spend many hours every day managing schedule changes</p>
    <div class="art art-after" role="img" aria-label="Icon of a clock beside a checked schedule document" style="left:756px;top:815px;width:230px;height:178px"></div>
    <p class="after-text" style="top:1001px">Schedules are optimized automatically and personnel have time for strategic planning and continuous improvement activities. Save up to 80% of planner time.</p>
    <div class="divider" style="top:1236px"></div>
  </section>

  <section class="row row-3">
    <div class="num" style="top:1304px">3.</div>
    <div class="art art-before" role="img" aria-label="Line icon of a stocked box with a circular arrow" style="left:212px;top:1259px;width:169px;height:153px"></div>
    <p class="before-text" style="top:1451px">Inventory and lead-times are excessive.</p>
    <div class="art art-after" role="img" aria-label="Icon of boxes moving on a conveyor belt" style="left:765px;top:1292px;width:221px;height:115px"></div>
    <p class="after-text" style="top:1439px">Flow is streamlined, Inventory and Lead Time are reduced by up to 50%.</p>
    <div class="divider" style="top:1614px"></div>
  </section>

  <section class="row row-4">
    <div class="num" style="top:1689px">4.</div>
    <div class="art art-before" role="img" aria-label="Line icon of a delivery truck and a parcel" style="left:173px;top:1738px;width:262px;height:151px"></div>
    <p class="before-text" style="top:1908px">Chaotic expediting is rampant, causing inefficiency and late shipments.</p>
    <div class="art art-after" role="img" aria-label="Icon of an open hand with rising arrows" style="left:770px;top:1652px;width:201px;height:183px"></div>
    <p class="after-text" style="top:1860px">Accurate, long terms schedule visibility allows for accurate order commitments and on-time shipments. Efficiency and customer service improve, increasing sales and profit margins.</p>
    <div class="divider" style="top:2114px"></div>
  </section>

  <section class="row row-5">
    <div class="num" style="top:2198px">5.</div>
    <div class="art art-before" role="img" aria-label="Line icon of a checklist marked with an error cross" style="left:239px;top:2153px;width:171px;height:153px"></div>
    <p class="before-text" style="top:2369px">Sales and operations planning decisions about capacity, staffing, overtime, and forecasts are difficult and error prone.</p>
    <div class="art art-after" role="img" aria-label="Icon of two hands joining puzzle pieces" style="left:716px;top:2150px;width:322px;height:113px"></div>
    <p class="after-text" style="top:2369px">Great decisions are made quickly with data-driven what-if simulations to evaluate alternatives against key metrics</p>
  </section>
</main>
</body>
</html>
```